TalkWell needs a Letterhead

We need a letterhead for our company "TalkWell Consultants". Logo is attached. The company color is Turquoise. Icons for website, scan logo for website, icons for address, e-mail and phone appreciated rather than just words.

```html
<!DOCTYPE html>
<html lang="en">
<head>
<meta charset="utf-8">
<title>TalkWell Consultants Letterhead</title>
<link rel="stylesheet" href="https://fonts.googleapis.com/css2?family=Open+Sans:wght@400&family=Tinos:wght@400;700&display=swap">
<style>
  :root {
    --paper: #fbfbfb;
    --brand-blue: #3a7fc1;
    --turquoise: #2a9bb0;
    --tint-blue: #d3e3ee;
    --tint-green: #e6efdc;
    --signature-tint: #d9e0e4;
    --ink: #4a4a4a;
    --ink-soft: #6a6a6a;
    --rule: #9cc9d3;
  }
  * { margin: 0; padding: 0; box-sizing: border-box; }
  html, body { width: 942px; height: 1200px; overflow: hidden; background: var(--paper); }
  .letterhead { position: relative; width: 942px; height: 1200px; overflow: hidden; background: var(--paper); font-family: "Tinos", "Times New Roman", serif; color: var(--ink); }

  .brand { position: absolute; left: 560px; top: 104px; display: flex; align-items: center; gap: 12px; }
  .brand-square { width: 30px; height: 30px; background: var(--brand-blue); }
  .brand-name { font-family: "Open Sans", Arial, sans-serif; font-weight: 400; font-size: 27px; color: var(--brand-blue); line-height: 1; }

  .letter { position: absolute; left: 125px; top: 350px; width: 738px; font-size: 12px; line-height: 24.5px; }
  .meta b { font-weight: 700; }
  .salutation { margin-top: 24.5px; }
  .letter p.body { text-align: justify; margin-bottom: 24.5px; }

  .accent-blue { position: absolute; left: 0; top: 811px; width: 113px; height: 242px; background: var(--tint-blue); }
  .accent-green { position: absolute; left: 176px; top: 887px; width: 171px; height: 313px; background: var(--tint-green); }

  .sign-block { position: absolute; left: 125px; top: 826px; font-size: 12px; line-height: 17px; color: var(--ink); }
  .signatory-name { text-transform: uppercase; }
  .signature { position: absolute; left: 125px; top: 890px; width: 252px; height: 118px; background: var(--signature-tint); opacity: 0.55; }

  .contact { position: absolute; left: 718px; top: 1080px; display: flex; }
  .contact-icons { display: flex; flex-direction: column; width: 20px; }
  .contact-icons svg { width: 14px; height: 14px; margin: 2px 0; display: block; }
  .contact-rule { width: 1px; background: var(--rule); margin: 0 9px 0 4px; }
  .contact-lines { font-family: "Open Sans", Arial, sans-serif; font-size: 11.5px; line-height: 18px; color: var(--ink-soft); }
</style>
</head>
<body>
<main class="letterhead">
  <header class="brand">
    <span class="brand-square"></span>
    <span class="brand-name">TalkWell Consultants</span>
  </header>

  <section class="letter">
    <div class="meta">
      <div><b>Data :</b> Mon , 25 / 3 / 2013</div>
      <div><b>Recipient :</b> Mr. Peter Lane Morrison</div>
    </div>
    <div class="salutation">Dear Mr. Peter Lane</div>
    <p class="body">LoTrem ipsum dolor sit amet, consectetur adipiscing elit. Praesent vulputate, neque ac accumsan suscipit, justo turpis volutpat nisl, tempus fermentum eros tortor et elit. Vivamus porttitor faucibus gravida. Quisque pharetra gravida luctus. Donec eget turpis libero. Ut ac dolor urna, quis tempor nunc. Donec vitae mauris purus, euismod eleifend nulla. Lorem ipsum dolor sit amet, consectetur adipiscing elit. Donec ut purus tellus. Aenean quis dignissim lacus. Vestibulum suscipit vehicula cursus. Suspendisse potenti. Ut in sem nisi. Sed et massa leo.</p>
    <p class="body">Fusce varius libero vel risus condimentum suscipit. Nullam tristique ultrices massa a volutpat. Donec sed dictum metus. Curabitur fringilla nibh eu ligula pharetra a interdum quam aliquam. Maecenas aliquam elit eu orci rutrum molestie. Proin nisl justo, varius a volutpat nec, ultricies sed sem. Nam sit amet imperdiet sem. Phasellus vitae mauris odio. Etiam in purus dui. Etiam ultricies, ante vel iaculis sodales, arcu leo adipiscing leo, sit amet mollis dui nisi non quam.</p>
    <p class="body">Suspendisse sagittis laoreet dolor, vitae rhoncus arcu volutpat quis. Vestibulum at placerat dolor. Vivamus eu lacus ut enim molestie consectetur. Quisque ac lorem vel orci sagittis sollicitudin. Nunc ut quam sem, quis volutpat libero. Cum sociis natoque penatibus et magnis dis parturient montes, nascetur ridiculus mus. Vestibulum ante ipsum primis in faucibus orci luctus et ultrices posuere cubilia Curae; Donec tempor velit in velit feugiat sit amet vulputate nisl posuere..</p>
  </section>

  <div class="accent-blue"></div>
  <div class="accent-green"></div>

  <div class="sign-block">
    <div class="signatory-name">Peter Lane</div>
    <div class="signatory-role">General director</div>
  </div>
  <div class="signature" role="img" aria-label="Handwritten signature of the general director"></div>

  <footer class="contact">
    <div class="contact-icons">
      <svg viewBox="0 0 14 14" aria-hidden="true"><path fill="var(--turquoise)" d="M7 1a4 4 0 0 0-4 4c0 3 4 8 4 8s4-5 4-8a4 4 0 0 0-4-4zm0 5.5A1.5 1.5 0 1 1 7 3.5a1.5 1.5 0 0 1 0 3z"/></svg>
      <svg viewBox="0 0 14 14" aria-hidden="true" style="margin-top:20px"><path fill="var(--turquoise)" d="M3.5 2l2 2.5-1.2 1.3a8 8 0 0 0 3.9 3.9l1.3-1.2 2.5 2-1.3 1.7C6.5 12 2 7.5 1.8 3.3z"/></svg>
      <svg viewBox="0 0 14 14" aria-hidden="true"><rect x="1.5" y="3" width="11" height="8" fill="var(--turquoise)"/><path d="M1.5 3.5 7 8l5.5-4.5" fill="none" stroke="var(--paper)" stroke-width="1"/></svg>
      <svg viewBox="0 0 14 14" aria-hidden="true"><circle cx="7" cy="7" r="5.5" fill="none" stroke="var(--turquoise)" stroke-width="1.4"/><path d="M1.5 7h11M7 1.5c-2.5 3-2.5 8 0 11M7 1.5c2.5 3 2.5 8 0 11" fill="none" stroke="var(--turquoise)" stroke-width="1"/></svg>
    </div>
    <div class="contact-rule"></div>
    <div class="contact-lines">
      <div>48 Harbor Lane</div>
      <div>Easton, 40512</div>
      <div>555 018 2294</div>
      <div>info@talkwell.com</div>
      <div>www.talkwell.com</div>
    </div>
  </footer>
</main>
</body>
</html>
```